Veltrane New Business Card Design IT Company

PLEASE CHECK ATTACHED PDF DOC FOR DETAILS. I have put exactly what I want to save time and finish the project asap thanks.

Veltrane Consulting is an Information Management Consulting company providing IT Professional Services Consulting services to both Public and private sector.
Need a Business Card Design to represent. It has to be Premium Raised Spot Glass finish.
Company Name: Veltrane Consulting
Company Website: veltrane-example.com.au
Company Slogan: High Performance Meets Excellence
Name on Card: Tom Risley
Title: Managing Partner
Email: Tom.Risley@veltrane-example.com.au
Phone: 0472836105

Company Logo is under construction from PixelGuild
Company Logo & Company Name Font Color should Match and have to Electric Aqua Blue
Company Logo at the Back Side of the Card
Card Background color preference: Slight Grey or Black to make the logo and company Name stand Out.

Any Questions please Ask.

Industry/Entity Type

Construction

Contact Information for Business Card

PLEASE CHECK ATTACHED PDF DOC FOR DETAILS. I have put exactly what I want to save time and finish the project asap thanks
Name on Card: Tom Risley
Title: Managing Partner
Phone: 0472836105

Requirements
Must have
• PLEASE CHECK ATTACHED PDF DOC FOR DETAILS. I have put exactly what I want to save time and finish the project asap thanks
• Company Logo, Company Name, Company website Company Slogan at the back side of the Card with custom dark blue front and back background
• Company Logo, Company Name , Company Website at the Front of the Card Title and Name email and phone in the front also in white color font
Should not have
• Should not Have Decorative or Script Fonts
• Its a IT company so must be professional no flowers or waterfalls etc

```html
<!DOCTYPE html>
<html lang="en">
<head>
<meta charset="utf-8">
<title>Veltrane Consulting – Business Card</title>
<link rel="stylesheet" href="https://fonts.googleapis.com/css2?family=Poppins:wght@600;700&family=Questrial&display=swap">
<style>
  :root {
    --navy-deep: #050a2e;
    --navy-glow: #13307a;
    --ink: #0e1440;
    --aqua: #3ec6ff;
    --band-blue: #1670e0;
    --band-cyan: #35d2ff;
    --paper: #ffffff;
    --page: #e9ebf0;
    --edge: #1a1f6b;
  }
  * { margin: 0; padding: 0; box-sizing: border-box; }
  html, body {
    width: 1200px; height: 679px; overflow: hidden;
    background: var(--page);
  }
  .card {
    position: relative;
    width: 1200px; height: 679px;
    border-radius: 50px;
    overflow: hidden;
    border: 1.5px solid var(--edge);
    background: var(--paper);
  }
  .card__night {
    position: absolute; left: 0; top: 0; width: 100%; height: 330px;
    background: radial-gradient(ellipse at 50% 30%, var(--navy-glow) 0%, var(--navy-deep) 70%);
  }
  .card__band {
    position: absolute; left: 0; top: 330px; width: 100%; height: 60px;
    background: linear-gradient(90deg, var(--band-blue), var(--band-cyan));
  }
  .brand {
    position: absolute; left: 0; right: 0; top: 112px;
    display: flex; justify-content: center; align-items: center; gap: 24px;
  }
  .brand__dot {
    width: 90px; height: 90px; border-radius: 50%;
    background: var(--aqua); flex: none;
  }
  .brand__name {
    font-family: "Poppins", sans-serif; font-weight: 600;
    font-size: 60px; line-height: 1; color: var(--aqua);
    white-space: nowrap;
  }
  .person { position: absolute; left: 96px; top: 482px; }
  .person__name {
    font-family: "Poppins", sans-serif; font-weight: 700;
    font-size: 76px; line-height: 1; color: var(--ink);
    letter-spacing: -0.5px; white-space: nowrap;
  }
  .person__title {
    font-family: "Questrial", sans-serif; font-size: 31px;
    color: var(--ink); margin-top: 8px;
  }
  .contacts {
    position: absolute; left: 560px; top: 466px;
    list-style: none;
  }
  .contacts__item {
    display: flex; align-items: center; height: 52px;
    font-family: "Questrial", sans-serif; font-size: 32px;
    color: var(--ink); white-space: nowrap;
  }
  .contacts__icon { width: 24px; height: 24px; fill: var(--ink); flex: none; }
  .contacts__rule {
    width: 2.5px; height: 32px; background: var(--ink);
    margin: 0 14px 0 12px; flex: none;
  }
</style>
</head>
<body>
<div class="card">
  <div class="card__night"></div>
  <div class="card__band" role="img" aria-label="Blue to cyan decorative band separating the dark header from the white panel"></div>

  <div class="brand">
    <span class="brand__dot"></span>
    <span class="brand__name">Veltrane Consulting</span>
  </div>

  <div class="person">
    <h1 class="person__name">Tom Risley</h1>
    <p class="person__title">Managing Partner</p>
  </div>

  <ul class="contacts">
    <li class="contacts__item">
      <svg class="contacts__icon" viewBox="0 0 24 24" aria-hidden="true"><path d="M7 1h10a2 2 0 0 1 2 2v18a2 2 0 0 1-2 2H7a2 2 0 0 1-2-2V3a2 2 0 0 1 2-2zm0 3v14h10V4zm5 15.2a1.2 1.2 0 1 0 0 2.4 1.2 1.2 0 0 0 0-2.4z"/></svg>
      <span class="contacts__rule"></span>0472 836 105
    </li>
    <li class="contacts__item">
      <svg class="contacts__icon" viewBox="0 0 24 24" aria-hidden="true"><path d="M2 6h20v13H2zm2 1.6 8 5.6 8-5.6z"/></svg>
      <span class="contacts__rule"></span>tom.risley@veltrane-example.com.au
    </li>
    <li class="contacts__item">
      <svg class="contacts__icon" viewBox="0 0 24 24" aria-hidden="true"><path d="M12 2a10 10 0 1 0 0 20 10 10 0 0 0 0-20zm0 2c.9 1.2 1.6 2.6 2 4h-4c.4-1.4 1.1-2.8 2-4zM4.3 14a8 8 0 0 1 0-4h3.5a14 14 0 0 0 0 4zm.9 2h3c.4 1.4 1 2.7 1.8 3.7A8 8 0 0 1 5.2 16zm3-8h-3a8 8 0 0 1 4.8-3.7C9.2 5.3 8.6 6.6 8.2 8zM12 20c-.9-1.2-1.6-2.6-2-4h4c-.4 1.4-1.1 2.8-2 4zm2.3-6H9.7a12 12 0 0 1 0-4h4.6a12 12 0 0 1 0 4zm.3 5.7c.8-1 1.4-2.3 1.8-3.7h3a8 8 0 0 1-4.8 3.7zM16.2 14a14 14 0 0 0 0-4h3.5a8 8 0 0 1 0 4z"/></svg>
      <span class="contacts__rule"></span>veltrane-example.com.au
    </li>
  </ul>
</div>
</body>
</html>
```